Fun Location App for users to earn rewards and vouchers everywhere they go

Tovrim is a social app where users can collect rewards when they travel + complete quests at different location to get rewards.

We would like a design of an app that has these features/function
1) Login/Signup Page
2) HomePage - A Map with your current location
- Show the location/stores aroudn
- Have a bag tab to press and get rewards
3) Quests Tab = show all the available tasks
4) Exchange Tab = all the items available for exchange vouchers and can click to know more
5) Wallet Tab = user profile + vouchers in their wallet
6) Partners Tab = Showcase all the partners and can click to know more
7) Claim functions

We have attached a visual example. Do feel free to change what is best fit too. We do need to exact measurements as well to create the app

Target Market(s)

Fun, people who like rewards and interact with friends

Font styles to use
Sans Serif

Colors
f78f20
fbed22
fbee3e

Requirements
Must have
• Yellow, fun interactive feeling.
Nice to have
• Pop up when click on things
Should not have
• nil

```html
<!DOCTYPE html>
<html lang="en">
<head>
<meta charset="utf-8">
<title>Tovrim – App Screens</title>
<link href="https://fonts.googleapis.com/css2?family=Poppins:wght@400;500;600;700&display=swap" rel="stylesheet">
<style>
:root{
  --orange:#f78f20;
  --yellow:#fbed22;
  --yellow-soft:#fbee3e;
  --ink:#2b2b2b;
  --muted:#8a8a8a;
  --line:#d6d6d6;
  --page:#f7f7f9;
  --map:#1c1c1c;
  --map-soft:#2a2a2a;
  --blue:#4267b2;
  --grad:linear-gradient(100deg,var(--orange) 0%,#f9b21e 55%,var(--yellow) 100%);
}
*{box-sizing:border-box;margin:0;padding:0}
html,body{width:1200px;height:2400px;overflow:hidden}
body{font-family:'Poppins',sans-serif;background:var(--page);color:var(--ink);position:relative}

/* hero */
.hero{position:absolute;left:0;top:0;width:1200px;height:676px;overflow:hidden;
  background:linear-gradient(120deg,var(--yellow-soft) 0%,#fbd02a 45%,var(--orange) 100%)}
.hero-card{position:absolute;width:200px;height:440px;background:#fff;border-radius:16px;
  transform:rotate(-32deg);box-shadow:0 20px 40px rgba(180,90,0,.25);overflow:hidden}
.hero-card .bar{height:92px;background:var(--grad);color:#fff;font-weight:700;font-size:30px;
  display:flex;align-items:center;justify-content:center}
.hero-card .ttl{color:var(--orange);font-weight:600;text-align:center;font-size:15px;margin:16px 0 10px}
.hero-card .fld{height:20px;border:1px solid var(--line);border-radius:20px;margin:10px 18px}
.hero-card .btn{height:22px;border-radius:4px;background:var(--grad);margin:14px 18px}
.hero-card.dark{background:linear-gradient(160deg,var(--map-soft),var(--map))}
.hero-card .row{display:flex;gap:8px;margin:12px 14px;align-items:center}
.hero-card .row i{width:40px;height:30px;border-radius:3px;background:linear-gradient(120deg,#6cbf3a,#f08a2a)}
.hero-card .row b{flex:1;height:6px;background:#e5e5e5;border-radius:3px}
.hero-card .row em{width:34px;height:10px;background:var(--orange);border-radius:6px}

/* grid */
.label{position:absolute;width:300px;text-align:center;font-size:19px;font-weight:500;color:#333}
.screen{position:absolute;width:214px;background:#fff;border-radius:14px;overflow:hidden;
  box-shadow:0 6px 22px rgba(0,0,0,.07)}
.head{background:var(--grad);color:#fff;text-align:center;border-radius:14px}
.head .welcome{font-size:10px;padding-top:26px}
.wordmark{font-weight:700;font-size:30px;line-height:1.1;letter-spacing:-.5px}
.form-title{color:var(--orange);font-weight:600;font-size:15px;text-align:center;margin:20px 0 14px;letter-spacing:.5px}
.input{height:22px;border:1px solid #c9c9c9;border-radius:20px;margin:0 17px 18px;font-size:8px;color:#666;
  padding-left:12px;display:flex;align-items:center}
.hint{font-size:6.5px;color:#777;margin:-12px 18px 14px}
.cta{height:25px;border-radius:3px;background:var(--grad);color:#fff;font-size:8.5px;font-weight:600;
  display:flex;align-items:center;justify-content:center;margin:0 17px;box-shadow:0 3px 6px rgba(247,143,32,.25)}
.social{height:24px;border-radius:3px;margin:16px 17px 0;font-size:7px;font-weight:500;display:flex;align-items:center;
  justify-content:center;position:relative}
.social .dot{position:absolute;left:12px;width:10px;height:10px;border-radius:50%}
.social.circlo{background:var(--blue);color:#fff}
.social.circlo .dot{background:#fff}
.social.seekr{background:#fff;color:#333;box-shadow:0 2px 6px rgba(0,0,0,.1)}
.social.seekr .dot{background:#e0463a}
.foot{position:absolute;left:0;right:0;text-align:center;font-size:7.5px;color:#444}
.foot a{color:var(--orange);font-weight:600;text-decoration:none}
.powered{position:absolute;left:0;right:0;bottom:7px;text-align:center;font-size:5.5px;color:#666;line-height:1.4}
.powered b{display:block;font-size:6.5px;color:#333}

.brand{display:flex;align-items:center;justify-content:center;gap:6px;font-weight:700;color:#333}
.brand i{width:16px;height:16px;border-radius:50%;background:var(--yellow);border:3px solid var(--orange)}

.map{position:absolute;background:linear-gradient(170deg,var(--map-soft) 0%,var(--map) 70%)}
.pin{position:absolute;width:18px;height:22px}
.gear{position:absolute;width:20px;height:20px}

.tabbar{position:absolute;left:0;right:0;bottom:0;height:42px;background:#fff;display:flex;
  justify-content:space-around;align-items:center;padding:0 8px}
.tabbar svg{width:18px;height:18px}

.bag{position:absolute;left:18px;right:18px;height:40px;background:#222;border-radius:6px;display:flex;align-items:center;
  padding:0 10px;color:#fff;box-shadow:0 4px 10px rgba(0,0,0,.4)}
.bag .stat{text-align:center;margin-right:22px;line-height:1}
.bag .stat b{font-size:15px;font-weight:600}
.bag .stat span{display:block;font-size:6.5px;margin-top:2px}
.bag .btn{margin-left:auto;width:26px;height:26px;border-radius:4px;background:var(--orange);display:flex;align-items:center;justify-content:center}

.tabhead{height:56px;background:var(--grad);border-radius:14px;color:#fff;padding:10px 14px;position:relative}
.tabhead h3{font-size:14px;font-weight:600;line-height:1.2}
.tabhead p{font-size:8px}
.tabhead .gear{right:14px;top:15px;width:18px;height:18px}
.list{padding:8px 11px 0}
.item{display:flex;align-items:center;gap:8px;height:55px}
.thumb{width:58px;height:40px;border-radius:2px;flex:none}
.t1{background:linear-gradient(110deg,#e84a3a 0%,#8bc34a 45%,#6ab04c 100%)}
.t2{background:linear-gradient(110deg,#f58b33,#f4b44a)}
.t3{background:linear-gradient(110deg,#7b2d1f,#c8563a 55%,#e8a070)}
.t4{background:linear-gradient(110deg,#f3ece3,#b0b7c2 60%,#3a4b6a)}
.item .txt{flex:1;line-height:1.3}
.item .txt b{display:block;font-size:8.5px;font-weight:600}
.item .txt span{display:block;font-size:7px;color:#444}
.item .txt small{display:block;font-size:5px;color:#999;border-top:1px solid #eee;margin-top:1px;padding-top:1px}
.pill{font-size:6.5px;color:#fff;background:var(--orange);border-radius:8px;padding:2px 7px;border:1px solid #f3b36d}

.card{background:#fff;margin:0 16px;border-radius:4px;box-shadow:0 2px 10px rgba(0,0,0,.06);padding:10px 11px}
.toggle{position:absolute;right:12px;top:10px;width:26px;height:12px;border-radius:8px;border:1.5px solid #aaa;background:#fff}
.toggle::after{content:"";position:absolute;top:1px;left:1px;width:7px;height:7px;border-radius:50%;background:#aaa}
.toggle.on{background:var(--orange);border-color:var(--orange)}
.toggle.on::after{left:auto;right:1px;background:#fff}
.card h4{font-size:10px;font-weight:500}
.card p{font-size:6px;color:#555;line-height:1.55;margin-top:6px}

.back{position:absolute;left:14px;top:16px;width:10px;height:10px}
</style>
</head>
<body>

<!-- hero band -->
<section class="hero">
  <div class="hero-card" style="left:60px;top:280px">
    <div class="bar">Tovrim</div><div class="ttl">SIGN IN</div>
    <div class="fld"></div><div class="fld"></div><div class="btn"></div>
    <div class="btn" style="background:var(--blue)"></div><div class="fld"></div>
  </div>
  <div class="hero-card" style="left:230px;top:-30px"><div style="height:100%;background:linear-gradient(150deg,#fff7d6,#fff 60%);display:flex;align-items:center;justify-content:center"><div class="brand" style="font-size:32px"><i></i>Tovrim</div></div></div>
  <div class="hero-card dark" style="left:390px;top:330px" role="img" aria-label="Dark city map of the home screen"></div>
  <div class="hero-card" style="left:470px;top:40px">
    <div class="bar" style="height:60px;font-size:16px">Quest Time !</div>
    <div class="row"><i></i><b></b><em></em></div><div class="row"><i></i><b></b><em></em></div>
    <div class="row"><i></i><b></b><em></em></div><div class="row"><i></i><b></b><em></em></div>
    <div class="row"><i></i><b></b><em></em></div><div class="row"><i></i><b></b><em></em></div>
  </div>
  <div class="hero-card" style="left:720px;top:80px">
    <div class="bar">Tovrim</div><div class="ttl">SIGN UP</div>
    <div class="fld"></div><div class="fld"></div><div class="fld"></div><div class="fld"></div><div class="fld"></div><div class="btn"></div>
  </div>
  <div class="hero-card" style="left:700px;top:470px">
    <div class="bar">Tovrim</div><div class="ttl">OTP LOG IN</div><div class="fld"></div><div class="fld"></div>
  </div>
  <div class="hero-card" style="left:960px;top:60px">
    <div class="bar" style="height:60px;font-size:16px">Trade</div>
    <div class="row"><i></i><b></b><em></em></div><div class="row"><i></i><b></b><em></em></div>
    <div class="row"><i></i><b></b><em></em></div><div class="row"><i></i><b></b><em></em></div>
    <div class="row"><i></i><b></b><em></em></div><div class="row"><i></i><b></b><em></em></div>
  </div>
  <div class="hero-card" style="left:980px;top:450px">
    <div style="padding:40px 24px"><div class="brand" style="font-size:18px"><i></i></div>
    <div style="font-size:12px;line-height:2.2;margin-top:14px;font-weight:500">Home<br>Partners<br>Guide<br>Terms of Use<br>Privacy Policy<br>Chat with Us</div></div>
  </div>
</section>

<!-- row 1 labels -->
<div class="label" style="left:25px;top:718px">Splash Screen</div>
<div class="label" style="left:310px;top:718px">OTP Login</div>
<div class="label" style="left:596px;top:718px">Login</div>
<div class="label" style="left:881px;top:718px">Menu</div>

<!-- splash -->
<div class="screen" style="left:68px;top:755px;height:461px;background:linear-gradient(170deg,#fff6d8 0%,#fffaf0 50%,#fff 100%)">
  <div style="position:absolute;left:12px;top:78px;width:190px;height:190px;border-radius:50%;background:#fff;display:flex;align-items:center;justify-content:center">
    <div class="brand" style="font-size:30px"><i></i>Tovrim</div>
  </div>
</div>

<!-- OTP login -->
<div class="screen" style="left:353px;top:755px;height:461px">
  <div class="head" style="height:112px"><div class="welcome">Welcome to</div><div class="wordmark">Tovrim</div></div>
  <div class="form-title">OTP LOG IN</div>
  <div class="input">Mobile No</div>
  <div class="input">Enter OTP</div>
  <div class="hint" style="text-align:center">Did not receive OTP ?</div>
  <div class="cta">Sign in</div>
  <div class="foot" style="bottom:36px">Don't have an account? <a>Sign Up</a></div>
  <div class="powered">Powered By<b>Harmonia Labs</b></div>
</div>

<!-- login -->
<div class="screen" style="left:638px;top:755px;height:461px">
  <div class="head" style="height:112px"><div class="welcome">Welcome to</div><div class="wordmark">Tovrim</div></div>
  <div class="form-title">SIGN IN</div>
  <div class="input">Email</div>
  <div class="input">Password</div>
  <div class="hint" style="text-align:right">Forgot password?</div>
  <div class="cta">Sign in</div>
  <div class="social circlo" style="margin-top:30px"><span class="dot"></span>Connect with Circlo</div>
  <div class="social seekr"><span class="dot"></span>Connect with Seekr</div>
  <div class="foot" style="bottom:36px">Don't have an account? <a>Sign Up</a></div>
  <div class="powered">Powered By<b>Harmonia Labs</b></div>
</div>

<!-- menu -->
<div class="screen" style="left:923px;top:755px;height:461px;background:#f3f3f3">
  <div class="map" style="left:0;top:0;width:60px;height:420px" role="img" aria-label="Dark city street map"></div>
  <div style="position:absolute;left:60px;top:0;right:0;bottom:0;background:#fff">
    <div class="brand" style="margin-top:46px;font-size:16px"><i style="width:26px;height:26px;border-width:5px"></i></div>
    <div style="margin:40px 0 0 26px;font-size:9.5px;font-weight:500;line-height:2.7">
      <div>▪&nbsp; Home</div><div>▪&nbsp; Parners</div><div>▪&nbsp; Guide</div>
      <div>▪&nbsp; Terms of Use</div><div>▪&nbsp; Privacy Policy</div><div>▪&nbsp; Chat with Us</div>
    </div>
    <div style="position:absolute;left:26px;top:375px;font-size:9.5px;font-weight:500">
      <svg width="11" height="11" viewBox="0 0 24 24" style="vertical-align:-1px"><circle cx="12" cy="12" r="7" fill="none" stroke="#333" stroke-width="4" stroke-dasharray="4 2"/></svg>&nbsp; Settings</div>
    <div style="position:absolute;left:10px;right:10px;top:402px;height:36px;background:#fff;box-shadow:0 2px 8px rgba(0,0,0,.1);border-radius:4px;display:flex;align-items:center;padding:0 8px;font-size:9px;font-weight:500">
      <span style="width:22px;height:22px;border-radius:50%;background:#cfcfcf;margin-right:6px"></span>Nickname
      <svg style="margin-left:auto" width="13" height="13" viewBox="0 0 24 24"><path d="M10 4H4v16h6M14 8l4 4-4 4M18 12H9" fill="none" stroke="#333" stroke-width="2"/></svg>
    </div>
  </div>
</div>

<!-- row 2 labels -->
<div class="label" style="left:25px;top:1255px">Sign Up</div>
<div class="label" style="left:310px;top:1255px">Home Screen : Empty Bag</div>
<div class="label" style="left:596px;top:1255px">Home Screen : Bag with Items</div>
<div class="label" style="left:881px;top:1255px">Settings</div>

<!-- sign up -->
<div class="screen" style="left:68px;top:1293px;height:526px">
  <div class="head" style="height:114px;padding-top:40px">
    <svg class="back" viewBox="0 0 10 10"><path d="M7 1L3 5l4 4" stroke="#fff" stroke-width="1.6" fill="none"/></svg>
    <div class="wordmark">Tovrim</div></div>
  <div class="form-title" style="margin:22px 0 22px">SIGN UP</div>
  <div class="input" style="margin-bottom:19px">Full Name</div>
  <div class="input" style="margin-bottom:19px">Username</div>
  <div class="input" style="margin-bottom:19px">Email</div>
  <div class="input" style="margin-bottom:19px">Date of Birth</div>
  <div class="input" style="margin-bottom:14px">Referral Code</div>
  <div style="display:flex;align-items:center;gap:8px;margin:0 17px 14px;font-size:8px;color:#555">
    <span style="padding:0 10px">Gender</span>
    <span style="padding:4px 12px;box-shadow:0 1px 5px rgba(0,0,0,.12)">Female</span>
    <span style="padding:4px 13px;background:var(--orange);color:#fff">Male</span>
  </div>
  <div class="cta">Sign Up</div>
  <div style="font-size:6.5px;color:#555;margin:16px 17px 0;line-height:1.45">By Signing up you have agreed to Terms of Use and Privacy Policy on Tovrim PVT LTD</div>
  <div class="powered">Powered By<b>Harmonia Labs</b></div>
</div>

<!-- home empty / items -->
<div class="screen" style="left:353px;top:1293px;height:459px">
  <div class="map" style="left:0;top:0;right:0;height:417px" role="img" aria-label="Dark city street map with nearby store markers"></div>
  <svg class="gear" style="right:14px;top:10px" viewBox="0 0 24 24"><circle cx="12" cy="12" r="7" fill="none" stroke="#fff" stroke-width="4" stroke-dasharray="4 2.2"/></svg>
  <svg class="pin" style="left:107px;top:47px" viewBox="0 0 18 22"><path d="M9 21C4 14 2 11 2 8a7 7 0 0114 0c0 3-2 6-7 13z" fill="var(--yellow)" stroke="var(--orange)" stroke-width="1.5"/><circle cx="9" cy="8" r="2.5" fill="#222"/></svg>
  <svg class="pin" style="left:70px;top:136px" viewBox="0 0 18 22"><path d="M9 21C4 14 2 11 2 8a7 7 0 0114 0c0 3-2 6-7 13z" fill="var(--yellow)" stroke="var(--orange)" stroke-width="1.5"/><circle cx="9" cy="8" r="2.5" fill="#222"/></svg>
  <svg class="pin" style="left:25px;top:246px" viewBox="0 0 18 22"><path d="M9 21C4 14 2 11 2 8a7 7 0 0114 0c0 3-2 6-7 13z" fill="var(--yellow)" stroke="var(--orange)" stroke-width="1.5"/><circle cx="9" cy="8" r="2.5" fill="#222"/></svg>
  <svg class="pin" style="left:132px;top:292px" viewBox="0 0 18 22"><path d="M9 21C4 14 2 11 2 8a7 7 0 0114 0c0 3-2 6-7 13z" fill="var(--yellow)" stroke="var(--orange)" stroke-width="1.5"/><circle cx="9" cy="8" r="2.5" fill="#222"/></svg>
  <span style="position:absolute;left:109px;top:248px;width:14px;height:14px;border-radius:50%;background:var(--orange);border:3px solid var(--yellow)"></span>
  <div class="bag" style="top:368px"><div class="stat"><b>0</b><span>Tovcoins</span></div><div class="stat"><b>0</b><span>Vouchers</span></div>
    <div class="btn"><svg width="12" height="12" viewBox="0 0 12 12"><rect x="1" y="4" width="10" height="7" rx="1" fill="#fff"/><path d="M4 4V3a2 2 0 014 0v1" stroke="#fff" fill="none"/></svg></div></div>
  <nav class="tabbar">
    <svg viewBox="0 0 18 18"><rect x="3" y="2" width="12" height="14" rx="1" fill="#555"/><path d="M6 7h6M6 10h6M6 13h4" stroke="#fff"/></svg>
    <svg viewBox="0 0 18 18"><path d="M3 6h10l-3-3M15 12H5l3 3" stroke="#555" stroke-width="2" fill="none"/></svg>
    <svg viewBox="0 0 18 22" style="height:22px"><path d="M9 21C4 14 2 11 2 8a7 7 0 0114 0c0 3-2 6-7 13z" fill="var(--yellow)" stroke="var(--orange)" stroke-width="1.5"/><circle cx="9" cy="8" r="2.5" fill="#fff"/></svg>
    <svg viewBox="0 0 18 18"><rect x="2" y="4" width="14" height="11" rx="2" fill="#555"/><rect x="10" y="8" width="6" height="4" fill="#fff"/></svg>
    <svg viewBox="0 0 18 18"><path d="M9 16L2 9a4 4 0 017-5 4 4 0 017 5z" fill="#555"/></svg>
  </nav>
</div>

<div class="screen" style="left:638px;top:1293px;height:459px">
  <div class="map" style="left:0;top:0;right:0;height:417px" role="img" aria-label="Dark city street map with nearby store markers"></div>
  <svg class="gear" style="right:14px;top:10px" viewBox="0 0 24 24"><circle cx="12" cy="12" r="7" fill="none" stroke="#fff" stroke-width="4" stroke-dasharray="4 2.2"/></svg>
  <svg class="pin" style="left:107px;top:47px" viewBox="0 0 18 22"><path d="M9 21C4 14 2 11 2 8a7 7 0 0114 0c0 3-2 6-7 13z" fill="var(--yellow)" stroke="var(--orange)" stroke-width="1.5"/><circle cx="9" cy="8" r="2.5" fill="#222"/></svg>
  <svg class="pin" style="left:70px;top:136px" viewBox="0 0 18 22"><path d="M9 21C4 14 2 11 2 8a7 7 0 0114 0c0 3-2 6-7 13z" fill="var(--yellow)" stroke="var(--orange)" stroke-width="1.5"/><circle cx="9" cy="8" r="2.5" fill="#222"/></svg>
  <svg class="pin" style="left:25px;top:246px" viewBox="0 0 18 22"><path d="M9 21C4 14 2 11 2 8a7 7 0 0114 0c0 3-2 6-7 13z" fill="var(--yellow)" stroke="var(--orange)" stroke-width="1.5"/><circle cx="9" cy="8" r="2.5" fill="#222"/></svg>
  <svg class="pin" style="left:132px;top:292px" viewBox="0 0 18 22"><path d="M9 21C4 14 2 11 2 8a7 7 0 0114 0c0 3-2 6-7 13z" fill="var(--yellow)" stroke="var(--orange)" stroke-width="1.5"/><circle cx="9" cy="8" r="2.5" fill="#222"/></svg>
  <span style="position:absolute;left:109px;top:248px;width:14px;height:14px;border-radius:50%;background:var(--orange);border:3px solid var(--yellow)"></span>
  <div class="bag" style="top:368px"><div class="stat"><b>5</b><span>Tovcoins</span></div><div class="stat"><b>5000</b><span>Vouchers</span></div>
    <div class="btn"><svg width="12" height="12" viewBox="0 0 12 12"><rect x="1" y="4" width="10" height="7" rx="1" fill="#fff"/><path d="M4 4V3a2 2 0 014 0v1" stroke="#fff" fill="none"/></svg></div></div>
  <nav class="tabbar">
    <svg viewBox="0 0 18 18"><rect x="3" y="2" width="12" height="14" rx="1" fill="#555"/><path d="M6 7h6M6 10h6M6 13h4" stroke="#fff"/></svg>
    <svg viewBox="0 0 18 18"><path d="M3 6h10l-3-3M15 12H5l3 3" stroke="#555" stroke-width="2" fill="none"/></svg>
    <svg viewBox="0 0 18 22" style="height:22px"><path d="M9 21C4 14 2 11 2 8a7 7 0 0114 0c0 3-2 6-7 13z" fill="var(--yellow)" stroke="var(--orange)" stroke-width="1.5"/><circle cx="9" cy="8" r="2.5" fill="#fff"/></svg>
    <svg viewBox="0 0 18 18"><rect x="2" y="4" width="14" height="11" rx="2" fill="#555"/><rect x="10" y="8" width="6" height="4" fill="#fff"/></svg>
    <svg viewBox="0 0 18 18"><path d="M9 16L2 9a4 4 0 017-5 4 4 0 017 5z" fill="#555"/></svg>
  </nav>
</div>

<!-- settings -->
<div class="screen" style="left:921px;top:1293px;height:459px;background:#f8f8f8">
  <div class="tabhead" style="height:40px;text-align:center;padding-top:11px">
    <svg class="back" style="top:14px" viewBox="0 0 10 10"><path d="M7 1L3 5l4 4" stroke="#fff" stroke-width="1.6" fill="none"/></svg>
    <h3>Settings</h3></div>
  <div class="card" style="position:relative;margin-top:40px"><h4>Sound</h4><span class="toggle"></span>
    <p>Enable the sound feature to make your experience with Tovrim more fun and exciting !</p></div>
  <div class="card" style="position:relative;margin-top:12px"><h4>Location</h4><span class="toggle on"></span>
    <p>Enable the location feature to collect Tovcoins and rewards everywhere you travel. Connect with your peers nearby to multiply your winnings.</p></div>
</div>

<!-- row 3 labels -->
<div class="label" style="left:25px;top:1863px">Quest Tab</div>
<div class="label" style="left:310px;top:1863px">Trade Tab</div>
<div class="label" style="left:596px;top:1863px">Profile : Swarm</div>
<div class="label" style="left:881px;top:1863px">Chat</div>

<!-- quest -->
<div class="screen" style="left:68px;top:1901px;height:461px">
  <div class="tabhead"><h3>Quest Time !</h3><p>Challenges to earn rewards !</p>
    <svg class="gear" viewBox="0 0 24 24"><circle cx="12" cy="12" r="7" fill="none" stroke="#fff" stroke-width="4" stroke-dasharray="4 2.2"/></svg></div>
  <div class="list">
    <div class="item"><span class="thumb t1" role="img" aria-label="Partner food promotion image"></span><div class="txt"><b>Brookfold</b><span>$1 off for any Item</span></div><span class="pill">Challenge</span></div>
    <div class="item"><span class="thumb t2" role="img" aria-label="Partner promotion banner"></span><div class="txt"><b>Brookfold</b><span>$1 off for any Item</span></div><span class="pill">Challenge</span></div>
    <div class="item"><span class="thumb t3" role="img" aria-label="Pizza dish photo"></span><div class="txt"><b>Brookfold</b><span>$1 off for any Item</span></div><span class="pill">Challenge</span></div>
    <div class="item"><span class="thumb t4" role="img" aria-label="Seasonal fashion promotion"></span><div class="txt"><b>Brookfold</b><span>$1 off for any Item</span></div><span class="pill">Challenge</span></div>
    <div class="item"><span class="thumb t1" role="img" aria-label="Partner food promotion image"></span><div class="txt"><b>Brookfold</b><span>$1 off for any Item</span></div><span class="pill">Challenge</span></div>
    <div class="item"><span class="thumb t2" role="img" aria-label="Partner promotion banner"></span><div class="txt"><b>Brookfold</b><span>$1 off for any Item</span></div><span class="pill">Challenge</span></div>
    <div class="item"><span class="thumb t3" role="img" aria-label="Pizza dish photo"></span><div class="txt"><b>Brookfold</b><span>$1 off for any Item</span></div><span class="pill">Challenge</span></div>
  </div>
  <nav class="tabbar">
    <svg viewBox="0 0 18 18"><rect x="3" y="2" width="12" height="14" rx="1" fill="var(--orange)"/><path d="M6 7h6M6 10h6M6 13h4" stroke="#fff"/></svg>
    <svg viewBox="0 0 18 18"><path d="M3 6h10l-3-3M15 12H5l3 3" stroke="#555" stroke-width="2" fill="none"/></svg>
    <svg viewBox="0 0 18 22" style="height:22px"><path d="M9 21C4 14 2 11 2 8a7 7 0 0114 0c0 3-2 6-7 13z" fill="var(--yellow)" stroke="var(--orange)" stroke-width="1.5"/><circle cx="9" cy="8" r="2.5" fill="#fff"/></svg>
    <svg viewBox="0 0 18 18"><rect x="2" y="4" width="14" height="11" rx="2" fill="#555"/><rect x="10" y="8" width="6" height="4" fill="#fff"/></svg>
    <svg viewBox="0 0 18 18"><path d="M9 16L2 9a4 4 0 017-5 4 4 0 017 5z" fill="#555"/></svg>
  </nav>
</div>

<!-- trade -->
<div class="screen" style="left:353px;top:1901px;height:461px">
  <div class="tabhead"><h3>Trade</h3><p>55000 Tovcoins</p>
    <svg class="gear" viewBox="0 0 24 24"><circle cx="12" cy="12" r="7" fill="none" stroke="#fff" stroke-width="4" stroke-dasharray="4 2.2"/></svg></div>
  <div class="list">
    <div class="item" style="height:65px"><span class="thumb t1" role="img" aria-label="Partner food promotion image"></span><div class="txt"><b>Brookfold</b><span>$0.50 off for any food Item</span><small>4000 Tovcoins</small></div><span class="pill">Get It</span></div>
    <div class="item" style="height:65px"><span class="thumb t2" role="img" aria-label="Partner promotion banner"></span><div class="txt"><b>Brookfold</b><span>$0.50 off for any food Item</span><small>4000 Tovcoins</small></div><span class="pill">Get It</span></div>
    <div class="item" style="height:65px"><span class="thumb t3" role="img" aria-label="Pizza dish photo"></span><div class="txt"><b>Brookfold</b><span>$0.50 off for any food Item</span><small>4000 Tovcoins</small></div><span class="pill">Get It</span></div>
    <div class="item" style="height:65px"><span class="thumb t4" role="img" aria-label="Seasonal fashion promotion"></span><div class="txt"><b>Brookfold</b><span>$0.50 off for any food Item</span><small>4000 Tovcoins</small></div><span class="pill">Get It</span></div>
    <div class="item" style="height:65px"><span class="thumb t1" role="img" aria-label="Partner food promotion image"></span><div class="txt"><b>Brookfold</b><span>$0.50 off for any food Item</span><small>4000 Tovcoins</small></div><span class="pill">Get It</span></div>
    <div class="item" style="height:65px"><span class="thumb t2" role="img" aria-label="Partner promotion banner"></span><div class="txt"><b>Brookfold</b><span>$0.50 off for any food Item</span></div><span class="pill">Get It</span></div>
  </div>
  <nav class="tabbar">
    <svg viewBox="0 0 18 18"><rect x="3" y="2" width="12" height="14" rx="1" fill="#555"/><path d="M6 7h6M6 10h6M6 13h4" stroke="#fff"/></svg>
    <svg viewBox="0 0 18 18"><path d="M3 6h10l-3-3M15 12H5l3 3" stroke="var(--orange)" stroke-width="2" fill="none"/></svg>
    <svg viewBox="0 0 18 22" style="height:22px"><path d="M9 21C4 14 2 11 2 8a7 7 0 0114 0c0 3-2 6-7 13z" fill="var(--yellow)" stroke="var(--orange)" stroke-width="1.5"/><circle cx="9" cy="8" r="2.5" fill="#fff"/></svg>
    <svg viewBox="0 0 18 18"><rect x="2" y="4" width="14" height="11" rx="2" fill="#555"/><rect x="10" y="8" width="6" height="4" fill="#fff"/></svg>
    <svg viewBox="0 0 18 18"><path d="M9 16L2 9a4 4 0 017-5 4 4 0 017 5z" fill="#555"/></svg>
  </nav>
</div>

<!-- profile -->
<div class="screen" style="left:638px;top:1901px;height:461px;background:#f8f8f8">
  <div class="tabhead" style="padding-left:66px">
    <span style="position:absolute;left:18px;top:9px;width:38px;height:38px;border-radius:50%;background:#ddd;border:2px solid #fff" role="img" aria-label="User profile photo"></span>
    <h3>Nickname</h3><p>55000 Tovcoins</p>
    <svg class="gear" viewBox="0 0 24 24"><circle cx="12" cy="12" r="7" fill="none" stroke="#fff" stroke-width="4" stroke-dasharray="4 2.2"/></svg></div>
  <div class="card" style="position:relative;margin:14px 8px 0;padding:14px 14px;font-size:7px;line-height:2;color:#333">
    <div style="font-size:10px;font-weight:500;margin-bottom:8px">Account</div>
    <span style="position:absolute;right:14px;top:12px;width:18px;height:18px;background:#333;border-radius:2px"></span>
    <div>☏&nbsp; +65 5550-0100</div><div>✉&nbsp; nickname@mailbox.test</div><div>Referral Code : <b>ebK3Q</b></div>
  </div>
  <div style="display:flex;margin:24px 8px 0;font-size:10px">
    <div style="flex:1;text-align:center;padding:7px 0;color:#444">Vouchers</div>
    <div style="flex:1;text-align:center;padding:7px 0;color:var(--orange);background:#fff">Swarm</div>
  </div>
  <div style="background:#fff;margin:0 8px;height:160px;text-align:center;padding-top:60px">
    <div style="color:var(--orange);font-weight:600;font-size:15px">Coming Soon !</div>
    <div style="font-size:7px;color:#444;line-height:1.5;margin-top:4px">Connect, Join and Form a Clan<br>with your friends and family</div>
  </div>
  <nav class="tabbar">
    <svg viewBox="0 0 18 18"><rect x="3" y="2" width="12" height="14" rx="1" fill="#555"/><path d="M6 7h6M6 10h6M6 13h4" stroke="#fff"/></svg>
    <svg viewBox="0 0 18 18"><path d="M3 6h10l-3-3M15 12H5l3 3" stroke="#555" stroke-width="2" fill="none"/></svg>
    <svg viewBox="0 0 18 22" style="height:22px"><path d="M9 21C4 14 2 11 2 8a7 7 0 0114 0c0 3-2 6-7 13z" fill="var(--yellow)" stroke="var(--orange)" stroke-width="1.5"/><circle cx="9" cy="8" r="2.5" fill="#fff"/></svg>
    <svg viewBox="0 0 18 18"><rect x="2" y="4" width="14" height="11" rx="2" fill="#555"/><rect x="10" y="8" width="6" height="4" fill="#fff"/></svg>
    <svg viewBox="0 0 18 18"><path d="M9 16L2 9a4 4 0 017-5 4 4 0 017 5z" fill="#555"/></svg>
  </nav>
</div>

<!-- chat -->
<div class="screen" style="left:924px;top:1901px;height:461px;background:#f8f8f8">
  <div class="tabhead" style="height:43px;text-align:center;padding-top:11px">
    <svg class="back" style="top:16px" viewBox="0 0 10 10"><path d="M7 1L3 5l4 4" stroke="#fff" stroke-width="1.6" fill="none"/></svg>
    <h3>Chat With Us</h3></div>
  <div style="font-size:8px;color:#444;line-height:1.5;margin:36px 18px 0">We love to have a chat with our users anytime !</div>
  <div style="font-size:8px;color:#444;line-height:1.5;margin:14px 18px 0">If you have any feedback, experience any error, or simply want to chat with us, reach out to us via the below channels</div>
  <div style="margin:14px 17px 0;height:36px;background:var(--blue);border-radius:3px;color:#fff;display:flex;align-items:center;padding-left:12px;gap:10px">
    <svg width="14" height="14" viewBox="0 0 14 14"><path d="M1 7l12-5-3 11-4-3z" fill="#fff"/></svg>
    <div style="line-height:1.2"><div style="font-size:5.5px">Chatline</div><div style="font-size:10px;font-weight:600">@tovrimassistant</div></div>
  </div>
  <div style="margin:16px 17px 0;height:36px;background:var(--grad);border-radius:3px;color:#fff;display:flex;align-items:center;padding-left:12px;gap:10px">
    <svg width="14" height="14" viewBox="0 0 14 14"><path d="M1 7l12-5-3 11-4-3z" fill="#fff"/></svg>
    <div style="line-height:1.2"><div style="font-size:5.5px">Email</div><div style="font-size:10px;font-weight:600">hello@tovrim.app</div></div>
  </div>
</div>

</body>
</html>
```